Brom-leigh Sky Harbour Custom Brokers Limited

Shop online from the USA and Ship to Jamaica
Customs Brokerage, Import Export and logistic Services
Address:- 238-240 Halden Brook Road Kingston Jamaica
Email: info@bromleighskyharbour,com
Web: www.bromleighskyharbour.com
Telephone: (876) 555-0148, (876) 555-0193
flyer should be quarter page must print information on back and front

```html
<!DOCTYPE html>
<html lang="en">
<head>
<meta charset="utf-8">
<title>Brom-leigh Sky Harbour – Quarter Page Flyer</title>
<link rel="stylesheet" href="https://fonts.googleapis.com/css2?family=Arimo:wght@400;700&family=Montserrat:wght@500;600;700&display=swap">
<style>
  :root {
    --navy: #1e2a48;
    --gold: #eeab17;
    --ink: #2a2f3a;
    --grey: #4a4f59;
    --line: #d9dbe0;
    --page: #d4d4d4;
    --white: #ffffff;
  }
  * { box-sizing: border-box; margin: 0; padding: 0; }
  html, body { width: 1200px; height: 1200px; overflow: hidden; }
  body { background: var(--page); font-family: Arimo, Arial, sans-serif; position: relative; }

  .flyer { position: absolute; top: 228px; width: 469px; height: 750px; overflow: hidden; background: var(--white); box-shadow: 0 4px 10px rgba(0,0,0,.25); }
  .flyer--front { left: 102px; }
  .flyer--back { left: 618px; }
  .layer { position: absolute; inset: 0; }

  .brand { position: absolute; display: flex; align-items: center; gap: 7px; font-family: Montserrat, Arial, sans-serif; }
  .brand__dot { width: 14px; height: 14px; border-radius: 50%; background: var(--gold); flex: none; }
  .brand__name { font-weight: 600; font-size: 15px; letter-spacing: .5px; }
  .brand__sub { font-family: Arimo, Arial, sans-serif; font-size: 9px; letter-spacing: 4.5px; color: #8a8f99; position: absolute; }

  /* front */
  .front-photo { background: linear-gradient(175deg, #ffffff 0%, #fff8ee 28%, #f7dcb8 45%, #d98a55 58%, #8b5a4a 70%, #3f6470 82%, #2d4d5a 100%); }
  .front .brand { left: 36px; top: 98px; color: var(--navy); }
  .headline { position: absolute; left: 30px; top: 144px; font-weight: 700; font-size: 35px; line-height: 41px; color: var(--gold); }
  .headline-rule { position: absolute; left: 32px; top: 270px; width: 36px; height: 3px; background: var(--gold); }
  .tagline { position: absolute; left: 31px; top: 280px; font-weight: 700; font-size: 17.5px; line-height: 22px; color: var(--navy); }
  .contact { position: absolute; color: var(--white); font-size: 13px; line-height: 16px; display: flex; gap: 6px; white-space: nowrap; }
  .contact__icon { width: 15px; height: 15px; border-radius: 50%; background: var(--gold); flex: none; display: flex; align-items: center; justify-content: center; margin-top: 1px; }
  .contact__icon svg { width: 9px; height: 9px; }
  .contact--narrow { font-size: 12.5px; }

  /* back */
  .back .brand { left: 26px; top: 66px; color: var(--white); }
  .back .brand__name { font-size: 10.5px; }
  .back .brand__dot { width: 10px; height: 10px; }
  .back .brand__sub { font-size: 7px; letter-spacing: 3px; color: #aab; }
  .welcome { position: absolute; left: 26px; top: 118px; font-family: Montserrat, Arial, sans-serif; font-weight: 700; color: var(--white); font-size: 21px; line-height: 24px; }
  .welcome span { display: block; color: var(--gold); font-size: 12.5px; font-weight: 600; letter-spacing: .4px; }
  .divider { position: absolute; left: 235px; top: 33px; width: 1px; height: 185px; background: #3b4a6e; }
  .intro { position: absolute; left: 252px; top: 31px; width: 204px; font-size: 11px; line-height: 13.3px; color: var(--white); }
  .section-title { position: absolute; left: 26px; top: 283px; font-weight: 700; font-size: 21.5px; color: var(--navy); }
  .section-title span { color: var(--gold); }
  .section-title::after { content: ""; position: absolute; left: 0; top: 30px; width: 49px; height: 3px; background: var(--navy); }
  .services-box { position: absolute; left: 20px; top: 410px; width: 429px; height: 137px; border: 1.5px solid var(--line); border-radius: 8px; }
  .service { position: absolute; top: 428px; width: 74px; margin-left: -37px; text-align: center; }
  .service__name { height: 30px; display: flex; align-items: flex-end; justify-content: center; font-weight: 700; font-size: 12px; line-height: 13px; color: var(--ink); letter-spacing: -.2px; white-space: nowrap; }
  .service__text { margin-top: 8px; font-size: 11.5px; line-height: 13.3px; color: var(--grey); }
  .back-photo { position: absolute; left: 0; top: 560px; width: 469px; height: 150px; background: linear-gradient(180deg, #ffffff 0%, #fbe6d2 35%, #f3c9a3 60%, #f6dcc4 100%); opacity: .85; }
</style>
</head>
<body>

<section class="flyer flyer--front front" aria-label="Flyer front">
  <div class="layer front-photo" role="img" aria-label="Aerial photo of a container ship at sea at sunset with stacked parcel boxes from online stores"></div>

  <div class="brand"><span class="brand__dot"></span><span class="brand__name">BROM-LEIGH SKY HARBOUR</span></div>
  <div class="brand__sub" style="left:50px;top:120px">Custom Brokers Ltd.</div>

  <h1 class="headline">Shop online<br>from the USA and<br>Ship to Jamaica</h1>
  <div class="headline-rule"></div>
  <p class="tagline">Customs Brokerage, Import Export<br>and logistic Services</p>

  <svg class="layer" width="469" height="750" viewBox="0 0 469 750" aria-hidden="true">
    <path d="M0 580 C80 630 160 658 240 650 C320 642 400 622 469 612 L469 750 L0 750 Z" fill="var(--gold)"/>
    <path d="M0 592 C80 640 160 664 240 658 C320 652 400 632 469 624 L469 750 L0 750 Z" fill="var(--white)"/>
    <path d="M0 598 C80 645 160 668 240 663 C320 658 400 638 469 630 L469 750 L0 750 Z" fill="var(--navy)"/>
  </svg>

  <div class="contact" style="left:25px;top:682px"><span class="contact__icon"><svg viewBox="0 0 10 10"><path d="M2 1l2 2-1 1.2c.6 1.2 1.5 2.1 2.8 2.8L7 6l2 2-1.3 1.3C4.5 9 1 5.5.7 2.3z" fill="#fff"/></svg></span>(876) 555-0148 / (876) 555-0193</div>
  <div class="contact" style="left:25px;top:704px"><span class="contact__icon"><svg viewBox="0 0 10 10"><path d="M5 .8a3 3 0 0 1 3 3c0 2.2-3 5.4-3 5.4S2 6 2 3.8a3 3 0 0 1 3-3z" fill="#fff"/><circle cx="5" cy="3.8" r="1.1" fill="var(--gold)"/></svg></span><span>238-240 Halden Brook Road<br>Kingston Jamaica</span></div>
  <div class="contact contact--narrow" style="left:248px;top:682px"><span class="contact__icon"><svg viewBox="0 0 10 10"><rect x="1" y="2.5" width="8" height="5.5" rx=".6" fill="#fff"/><path d="M1.3 2.8 5 5.6l3.7-2.8" stroke="var(--gold)" stroke-width=".9" fill="none"/></svg></span>info@bromleighskyharbour,com</div>
  <div class="contact contact--narrow" style="left:248px;top:704px"><span class="contact__icon"><svg viewBox="0 0 10 10"><circle cx="5" cy="5" r="3.8" stroke="#fff" stroke-width="1" fill="none"/><path d="M1.2 5h7.6M5 1.2c-2 2.4-2 5.2 0 7.6M5 1.2c2 2.4 2 5.2 0 7.6" stroke="#fff" stroke-width=".8" fill="none"/></svg></span>www.bromleighskyharbour.com</div>
</section>

<section class="flyer flyer--back back" aria-label="Flyer back">
  <div class="back-photo" role="img" aria-label="Soft faded photo of a container port at sunrise"></div>

  <svg class="layer" width="469" height="750" viewBox="0 0 469 750" aria-hidden="true">
    <path d="M0 0 H469 V310 C420 262 370 240 300 238 C200 236 120 250 60 225 C30 212 10 195 0 170 Z" fill="var(--navy)"/>
    <path d="M0 170 C10 195 30 212 60 225 C120 250 200 236 300 238 C370 240 420 262 469 310 L469 298 C420 250 370 226 300 226 C200 226 120 240 60 214 C30 200 10 185 0 160 Z" fill="var(--gold)"/>
    <path d="M0 170 C15 205 40 225 80 240 C130 258 170 260 210 250 C150 255 100 245 60 225 C30 212 10 195 0 170 Z" fill="var(--gold)"/>
    <path d="M0 675 C140 695 320 680 469 600 L469 750 L0 750 Z" fill="var(--gold)"/>
    <path d="M0 690 C150 705 320 692 469 622 L469 750 L0 750 Z" fill="var(--white)"/>
    <path d="M0 697 C150 712 320 700 469 632 L469 750 L0 750 Z" fill="var(--navy)"/>
  </svg>

  <div class="brand"><span class="brand__dot"></span><span class="brand__name">BROM-LEIGH SKY HARBOUR</span></div>
  <div class="brand__sub" style="left:42px;top:84px">Custom Brokers Ltd.</div>
  <h2 class="welcome">WELCOME TO<span>BROM-LEIGH SKY HARBOUR</span></h2>
  <div class="divider"></div>
  <p class="intro">Sed ut perspiciatis unde omnis iste natus error sit voluptatem accusantium dol orem que laudantium, totam rem aperiam, eaque ipsa quae ab illo invent ore veritatis et quasi architecto beatae vitae dicta sunt explicabo. Nemo enim ipsam voluptatem quia volupt as sit aspernatur aut odit aut fugit, sed quia consequunt ur magni dolores eos qui ratione voluptatem sequi nesciunt. Neque porro quisquam est, qui dolorem ipsum quia dolor sit amet, consectetur, adipisci velit, sed quia non numquam eius modi.</p>

  <h3 class="section-title">OUR <span>SERVICES</span></h3>

  <div class="services-box"></div>
  <svg class="layer" width="469" height="750" viewBox="0 0 469 750" aria-hidden="true" fill="none" stroke-linecap="round" stroke-linejoin="round">
    <line x1="60" y1="410" x2="408" y2="410" stroke="var(--gold)" stroke-width="5"/>
    <line x1="148" y1="410" x2="200" y2="410" stroke="var(--navy)" stroke-width="5"/>
    <line x1="322" y1="410" x2="370" y2="410" stroke="var(--navy)" stroke-width="5"/>
    <g stroke-width="1.4">
      <path d="M60 335a27 27 0 0 1 8 52.8L60 396l-8-8.2A27 27 0 0 1 60 335z" stroke="var(--gold)" fill="#fff"/>
      <path d="M148 335a27 27 0 0 1 8 52.8L148 396l-8-8.2A27 27 0 0 1 148 335z" stroke="var(--navy)" fill="#fff"/>
      <path d="M234 335a27 27 0 0 1 8 52.8L234 396l-8-8.2A27 27 0 0 1 234 335z" stroke="var(--gold)" fill="#fff"/>
      <path d="M322 335a27 27 0 0 1 8 52.8L322 396l-8-8.2A27 27 0 0 1 322 335z" stroke="var(--navy)" fill="#fff"/>
      <path d="M408 335a27 27 0 0 1 8 52.8L408 396l-8-8.2A27 27 0 0 1 408 335z" stroke="var(--gold)" fill="#fff"/>
    </g>
    <g stroke-width="4" fill="#fff">
      <circle cx="60" cy="410" r="7" stroke="var(--gold)"/>
      <circle cx="148" cy="410" r="7" stroke="var(--navy)"/>
      <circle cx="234" cy="410" r="7" stroke="var(--gold)"/>
      <circle cx="322" cy="410" r="7" stroke="var(--navy)"/>
      <circle cx="408" cy="410" r="7" stroke="var(--gold)"/>
    </g>
    <g stroke="var(--gold)" stroke-width="1.3">
      <path d="M46 356h18v15H46zM64 361h6l4 5v5h-10"/><circle cx="51" cy="373" r="2.4"/><circle cx="69" cy="373" r="2.4"/>
    </g>
    <g stroke="var(--navy)" stroke-width="1.3">
      <path d="M134 372v-16h8l4 8h6v8zM152 356v16M152 372h10"/><rect x="156" y="362" width="8" height="7"/><circle cx="138" cy="374" r="2.4"/><circle cx="148" cy="374" r="2.4"/>
    </g>
    <g stroke="var(--gold)" stroke-width="1.3">
      <path d="M224 352h12v18h-12zM233 360h12v18h-12z"/><path d="M227 357h6M227 361h6M236 366h6M236 370h6"/>
    </g>
    <g stroke="var(--navy)" stroke-width="1.4">
      <path d="M318 360h-8v16h22v-6"/><path d="M316 370c2-8 8-11 16-11M328 354l5 5-5 5"/>
    </g>
    <g stroke="var(--gold)" stroke-width="1.1">
      <circle cx="408" cy="362" r="7"/><path d="M401 362h14M408 355c-3 4-3 10 0 14M408 355c3 4 3 10 0 14"/>
      <path d="M396 350l4 4M420 350l-4 4M396 374l4-4M420 374l-4-4"/>
    </g>
  </svg>

  <div class="service" style="left:60px"><div class="service__name">SHIPPING</div><p class="service__text">Sed ut perspiciatis unde omnis iste natus error</p></div>
  <div class="service" style="left:148px"><div class="service__name">LOGISTICS</div><p class="service__text">Sed ut perspiciatis unde omnis iste natus error</p></div>
  <div class="service" style="left:234px"><div class="service__name">CUSTOMS<br>CLEARANCE</div><p class="service__text">Sed ut perspiciatis unde omnis iste natus error</p></div>
  <div class="service" style="left:322px"><div class="service__name">IMPORTS</div><p class="service__text">Sed ut perspiciatis unde omnis iste natus error</p></div>
  <div class="service" style="left:408px"><div class="service__name">IMPORTS</div><p class="service__text">Sed ut perspiciatis unde omnis iste natus error</p></div>

  <div class="contact" style="left:15px;top:716px"><span class="contact__icon" style="width:20px;height:20px;margin-top:-2px"><svg viewBox="0 0 10 10"><path d="M2 1l2 2-1 1.2c.6 1.2 1.5 2.1 2.8 2.8L7 6l2 2-1.3 1.3C4.5 9 1 5.5.7 2.3z" fill="#fff"/></svg></span>(876) 555-0148 / (876) 555-0193</div>
  <div class="contact contact--narrow" style="left:250px;top:717px"><span class="contact__icon" style="width:20px;height:20px;margin-top:-2px"><svg viewBox="0 0 10 10"><circle cx="5" cy="5" r="3.8" stroke="#fff" stroke-width="1" fill="none"/><path d="M1.2 5h7.6M5 1.2c-2 2.4-2 5.2 0 7.6M5 1.2c2 2.4 2 5.2 0 7.6" stroke="#fff" stroke-width=".8" fill="none"/></svg></span>www.bromleighskyharbour.com</div>
</section>

</body>
</html>
```